BrightHarbor Flowchart Marketing Flyer

We are an MSP IT company. We have created a flowchart that we would like jazzed up to use in marketing new customers. The flowchart is a visual for prospective clients to see, in a simple way, what our process is. The flowchart should be 8.5"x11". We do not want the template of the flowchart altered (no boxes moved around) but would like something visually appealing and clean looking. Our office colors are lime green, royal blue, with accent colors of orange and purple. We would like the colors incorporated into the design. The design should be modern. This flyer is not going to be mass mailed. It will be handed to a prospective client in a face to face meeting.
Updates

I have uploaded our company logo to my brief in a couple of formats. One of the designers requested this. Great idea! I apologize for not providing it to begin with - it's my first time using this Website and the first time I have been assigned a project.

I was not able to view over the weekend as I did not have access to my work computer. Also need to review with the rest of management team on Thursday 6/28

Target Market(s)

Potential clients for an MSP IT company

Industry/Entity Type

It Company

Requirements
Must have
• The template itself we don't want changed. In other words we don't want the boxes moved around.
Nice to have
• Text, lines, shading and color of boxes can be changed. Not all colors mentioned in the brief need to be used. Would like it easy on the eye.

```html
<!DOCTYPE html>
<html lang="en">
<head>
<meta charset="utf-8">
<title>BrightHarbor Process</title>
<link href="https://fonts.googleapis.com/css2?family=Carlito:wght@400;700&display=swap" rel="stylesheet">
<style>
:root{
  --purple:#7030a0;
  --orange:#ed7d31;
  --green:#70ad47;
  --royal:#2f5597;
  --ink:#111;
  --line:#5b7fa6;
  --white:#fff;
}
*{margin:0;padding:0;box-sizing:border-box}
html,body{width:1200px;height:1200px;overflow:hidden;background:var(--white)}
body{font-family:"Carlito",Calibri,sans-serif;position:relative}
.band{
  position:absolute;left:0;top:262px;width:1200px;height:676px;
  background:
    radial-gradient(circle at 100% 0%, #b99ad0 0, rgba(185,154,208,0) 22%),
    radial-gradient(circle at 0% 100%, #5b9bd5 0, rgba(91,155,213,0) 40%),
    radial-gradient(ellipse at 55% 5%, #ee8a3c 0, rgba(238,138,60,0) 38%),
    radial-gradient(ellipse at 100% 62%, #ed8a3e 0, rgba(237,138,62,0) 30%),
    radial-gradient(ellipse at 10% 20%, #74ae46 0, rgba(116,174,70,0) 45%),
    radial-gradient(ellipse at 55% 85%, #72ae48 0, rgba(114,174,72,0) 45%),
    #9ca548;
}
.title{position:absolute;left:232px;top:290px;font-weight:700;font-size:30px;color:var(--ink)}
.step{
  position:absolute;display:flex;align-items:center;justify-content:center;text-align:center;
  color:var(--white);font-size:19px;line-height:1.25;border:1.5px solid #222;
  box-shadow:2px 3px 4px rgba(0,0,0,.35);
}
.step--assess{left:57px;top:418px;width:161px;height:86px;background:var(--purple)}
.step--onboard{left:293px;top:419px;width:161px;height:85px;background:var(--orange)}
.step--eval{left:526px;top:417px;width:161px;height:85px;background:var(--green)}
.cycle{position:absolute;left:765px;top:313px;width:376px;height:305px;background:var(--royal);border:3px solid #000}
.cycle__heading{position:absolute;left:0;right:0;top:9px;text-align:center;color:var(--white);font-weight:700;font-size:19px}
.phase{
  position:absolute;display:flex;align-items:center;justify-content:center;text-align:center;
  background:var(--orange);color:var(--ink);font-size:16px;line-height:1.3;border:1px solid #222;
  box-shadow:2px 3px 4px rgba(0,0,0,.4);
}
.phase--strategy{left:898px;top:373px;width:98px;height:54px}
.phase--risk{left:794px;top:441px;width:99px;height:56px}
.phase--standards{left:1010px;top:441px;width:98px;height:56px}
.phase--budget{left:897px;top:516px;width:98px;height:55px}
.links{position:absolute;left:0;top:0;width:1200px;height:1200px}
.tasks{position:absolute;list-style:none;font-size:13.5px;line-height:18px;color:var(--ink)}
.tasks li{position:relative}
.tasks li::before{content:"•";position:absolute;left:-11px}
.tasks--assess{left:73px;top:549px}
.tasks--assess li::before{left:-12px}
.tasks--onboard{left:304px;top:549px}
.tasks--onboard li::before{left:-9px}
.tasks--eval{left:533px;top:547px}
.tasks--eval li::before{left:-9px}
.tasks--cycle{left:790px;top:658px}
.tasks--cycle li::before{left:-15px}
sup{font-size:8px}
</style>
</head>
<body>
<div class="band"></div>
<h1 class="title">BrightHarbor Process</h1>

<svg class="links" viewBox="0 0 1200 1200" aria-hidden="true">
  <defs>
    <marker id="head" markerWidth="8" markerHeight="8" refX="7" refY="4" orient="auto">
      <path d="M0,0 L8,4 L0,8 z" fill="#000"/>
    </marker>
  </defs>
  <g stroke="#000" stroke-width="2.2" fill="none" marker-end="url(#head)">
    <line x1="221" y1="459" x2="290" y2="458"/>
    <line x1="455" y1="460" x2="524" y2="459"/>
    <line x1="690" y1="462" x2="760" y2="461"/>
  </g>
  <g stroke="var(--line)" stroke-width="1" fill="none">
    <polyline points="137,504 137,541 54,541 54,608"/>
    <polyline points="373,504 373,541 290,541 290,626"/>
    <polyline points="610,502 610,541 514,541 514,626"/>
    <polyline points="953,618 953,646 766,646 766,756"/>
  </g>
</svg>

<div class="step step--assess">Assess<br>Alignment</div>
<div class="step step--onboard">On Boarding</div>
<div class="step step--eval">30 Day<br>Evaluation</div>

<section class="cycle">
  <h2 class="cycle__heading">Ongoing Strategic Plan &amp; Execution</h2>
</section>
<svg class="links" viewBox="0 0 1200 1200" aria-hidden="true">
  <g stroke="#000" stroke-width="3" fill="none">
    <path d="M834,430 Q834,390 876,388"/>
    <path d="M1014,387 Q1055,390 1055,430"/>
    <path d="M834,506 Q836,549 874,549"/>
    <path d="M1050,506 Q1050,545 1010,547"/>
  </g>
</svg>
<div class="phase phase--strategy">Strategy</div>
<div class="phase phase--risk">Risk<br>Assessment</div>
<div class="phase phase--standards">Standards<br>Alignment</div>
<div class="phase phase--budget">Budget</div>

<ul class="tasks tasks--assess">
  <li>Review Technology Philosophy</li>
  <li>Share Proprietary Method</li>
  <li>Assess Organizational Fit</li>
</ul>
<ul class="tasks tasks--onboard">
  <li>Establish Expectations</li>
  <li>Service Provider Transition</li>
  <li>Cybersecurity Review</li>
  <li>Backup/Protection Strategy</li>
</ul>
<ul class="tasks tasks--eval">
  <li>Develop IT Playbook</li>
  <li>Major Risk Identification</li>
  <li>Observe &amp; Document Trends</li>
  <li>Standards Alignment Plan</li>
</ul>
<ul class="tasks tasks--cycle">
  <li>Develop &amp; Execute Annual Strategic Plan</li>
  <li>Risk Assessment, Ranking, Mitigation</li>
  <li>Prioritize Investments</li>
  <li>Develop 5 Year Budget</li>
  <li>HarborPath<sup>TM</sup> Standard Alignment</li>
</ul>
</body>
</html>
```